Ribbon Cutting Ceremony Invitation for Solar Company

Need 8.5 x 11 Ribbon Cutting Invitation Design to be used for digital and print. The design should be professional yet creative. It should showcase the theme of a ribbon cutting with some sort of style resembling solar energy. There could also be an option to include a placeholder for a photo of the facility, but that is up to your creative direction. Thanks designers!

Words that should be on it are below:

RIBBON CUTTING CEREMONY

WE FORMALLY INVITE YOU TO THE RIBBON CUTTING EVENT FOR THE NEW SOLAR SYSTEM @ SEABRAMBLE HOTEL AND RESORT.

DATE AND TIME

Use this logo in one of the corners: https://files.plenvarq-media.net/assets/k/kd/Vexa_Energy.png - Let me know if you need it in a different version, transparent, or all white.

PLEASE ASK ME ANY QUESTIONS!!!

Target Market(s)

Business Owners and Executives

Colors

Designer to choose colors to be used in the design.

Requirements
Must have
• Professional design with ribbon cutting and solar theme.

```html
<!DOCTYPE html>
<html lang="en">
<head>
<meta charset="utf-8">
<title>Ribbon Cutting Ceremony Invitation</title>
<link rel="stylesheet" href="https://fonts.googleapis.com/css2?family=Antonio:wght@100;700&family=Josefin+Sans:wght@400&display=swap">
<style>
  :root {
    --page-bg: #e6e6e8;
    --card-bg: #ffffff;
    --title-blue: #2b8fd4;
    --ink: #111111;
    --date-red: #c3202b;
    --date-text: #ffffff;
    --sky-top: #8fb8d9;
    --sky-mid: #c9d7e3;
    --sky-glow: #f0b57c;
    --panel-blue: #5f90c6;
    --panel-deep: #3f6fa8;
    --tab-border: #8a8a8a;
  }
  * { margin: 0; padding: 0; box-sizing: border-box; }
  html, body {
    width: 856px;
    height: 1200px;
    overflow: hidden;
    background: var(--page-bg);
  }
  .invitation {
    position: absolute;
    left: 0;
    top: 46px;
    width: 856px;
    height: 1108px;
    background: var(--card-bg);
    overflow: hidden;
  }
  .title-top {
    position: absolute;
    left: 0;
    width: 100%;
    top: 68px;
    text-align: center;
    font-family: "Antonio", "Arial Narrow", sans-serif;
    font-weight: 700;
    font-size: 92px;
    line-height: 1.2;
    letter-spacing: 3.5px;
    color: var(--title-blue);
    white-space: nowrap;
  }
  .title-main {
    position: absolute;
    left: 0;
    width: 100%;
    top: 166px;
    text-align: center;
    font-family: "Antonio", "Arial Narrow", sans-serif;
    font-weight: 100;
    font-size: 157px;
    line-height: 1.1;
    letter-spacing: 5px;
    color: var(--ink);
    white-space: nowrap;
  }
  .invite-text {
    position: absolute;
    left: 140px;
    width: 576px;
    top: 374px;
    font-family: "Josefin Sans", "Helvetica", sans-serif;
    font-weight: 400;
    font-size: 28px;
    line-height: 46px;
    color: var(--ink);
  }
  .invite-line {
    display: block;
    white-space: nowrap;
    text-align: justify;
    text-align-last: justify;
  }
  .invite-line.last {
    text-align: center;
    text-align-last: center;
  }
  .scene-photo {
    position: absolute;
    left: 0;
    top: 620px;
    width: 856px;
    height: 488px;
    background: linear-gradient(180deg,
      var(--sky-top) 0%,
      var(--sky-mid) 38%,
      var(--sky-glow) 62%,
      var(--panel-blue) 80%,
      var(--panel-deep) 100%);
  }
  .date-badge {
    position: absolute;
    left: 500px;
    top: 570px;
    width: 272px;
    height: 272px;
    border-radius: 50%;
    background: var(--date-red);
    color: var(--date-text);
    font-family: "Antonio", "Arial Narrow", sans-serif;
    font-weight: 700;
    text-align: center;
  }
  .date-day {
    position: absolute;
    left: 0; width: 100%;
    top: 12px;
    font-size: 126px;
    line-height: 1;
  }
  .date-month {
    position: absolute;
    left: 0; width: 100%;
    top: 146px;
    font-size: 36px;
    line-height: 1;
  }
  .date-year {
    position: absolute;
    left: 0; width: 100%;
    top: 187px;
    font-size: 53px;
    line-height: 1;
  }
  .brand-tab {
    position: absolute;
    left: 44px;
    top: 988px;
    width: 177px;
    height: 130px;
    background: var(--card-bg);
    border: 2px solid var(--tab-border);
    border-radius: 18px 18px 0 0;
    display: flex;
    align-items: center;
    justify-content: center;
    padding-bottom: 8px;
  }
  .brand-name {
    font-family: "Josefin Sans", "Helvetica", sans-serif;
    font-weight: 400;
    font-size: 24px;
    color: var(--ink);
    white-space: nowrap;
  }
</style>
</head>
<body>
  <main class="invitation">
    <h1 class="title-top">RIBBON CUTTING</h1>
    <h2 class="title-main">CEREMONY</h2>
    <p class="invite-text">
      <span class="invite-line">WE FORMALLY INVITE YOU TO THE</span>
      <span class="invite-line">RIBBON CUTTING EVENT FOR THE</span>
      <span class="invite-line">NEW SOLAR SYSTEM @ SEABRAMBLE</span>
      <span class="invite-line last">HOTEL AND RESORT.</span>
    </p>

    <div class="scene-photo" role="img" aria-label="Photo of rooftop solar panels under a sunset sky with a city skyline, with a red ribbon being cut by scissors"></div>

    <div class="date-badge">
      <span class="date-day">11</span>
      <span class="date-month">MARCH</span>
      <span class="date-year">2020</span>
    </div>

    <div class="brand-tab">
      <span class="brand-name">Vexa Power</span>
    </div>
  </main>
</body>
</html>
```